Christmas Card Design

I would like to have a design created for a no-fold card, two sided that will be printed on card stock. I would like to have the front be four polaroid pictures (I will supply the photos that will be inserted into the polaroid pic design, with text on top of the group of four and on the bottom. I would like the header text to read "Home is where our hearts are!" and the Footer text to read "Holiday love and magic from our home to yours, The Fairbrooks"
I would like the back to be one polaroid in the middle. If you would like to give this project a whirl, message me and I will send the photos. Each photo will have text in the bottom of the polaroid (typically the white part of a polaroid pic.)
1) Gwen, Washington, DC 2017
2) Artie, New York City 2017
3) Marisa, Chicago 2017
4) Kurt, Worcester, MA 2017
The photo on the back will have the following text:
Phil and Greta
Wilmette, IL 2017

```html
<!DOCTYPE html>
<html lang="en">
<head>
<meta charset="utf-8">
<title>Home is where our hearts are – Holiday Card</title>
<link rel="stylesheet" href="https://fonts.googleapis.com/css2?family=Oswald:wght@300;400;500;600;700&display=swap">
<style>
  :root {
    --backdrop: #e9e4df;
    --card-mint: #e3efe6;
    --card-cream: #f3f1ea;
    --card-blush: #f6dfe2;
    --berry: #c8235f;
    --heart: #f27b86;
    --heart-soft: #f5b3b4;
    --frame: #fbf9f1;
    --photo: #33393b;
    --ink: #3a3a3a;
    --string: #ffffff;
  }
  * { box-sizing: border-box; margin: 0; padding: 0; }
  html, body { width: 1200px; height: 843px; overflow: hidden; background: var(--backdrop); }
  .stage { position: relative; width: 1200px; height: 843px; font-family: "Oswald", sans-serif; }

  .card {
    position: absolute;
    overflow: hidden;
    background:
      radial-gradient(ellipse at 55% 60%, var(--card-cream) 0%, rgba(243,241,234,0) 55%),
      linear-gradient(120deg, var(--card-blush) 0%, var(--card-mint) 35%, var(--card-cream) 65%, var(--card-blush) 100%);
    box-shadow: 0 4px 10px rgba(0,0,0,.18);
  }
  .card--back  { left: 287px; top: 326px; width: 585px; height: 415px; }
  .card--front { left: 558px; top: 97px;  width: 587px; height: 415px; }

  .heart { position: absolute; fill: var(--heart); }
  .heart--soft { fill: var(--heart-soft); opacity: .75; }

  .line { position: absolute; left: 0; width: 100%; height: 30px; }

  .polaroid {
    position: absolute;
    background: var(--frame);
    box-shadow: 0 2px 5px rgba(0,0,0,.28);
    text-align: center;
    color: var(--ink);
  }
  .polaroid__photo { position: absolute; background: var(--photo); }
  .polaroid__clip {
    position: absolute; top: -8px; left: 50%; width: 8px; height: 12px;
    margin-left: -4px; background: #2a2a2a; border-radius: 1px;
  }
  .polaroid__name, .polaroid__place { position: absolute; left: 0; width: 100%; line-height: 1; }

  /* Front card */
  .headline {
    position: absolute; left: 80px; top: 18px; width: 440px;
    color: var(--berry); font-weight: 600; font-size: 53px; line-height: 50px;
  }
  .headline__row { display: block; }
  .headline__row--second { text-align: right; }
  .headline__soft { font-weight: 300; }

  .polaroid--small { width: 116px; height: 134px; }
  .polaroid--small .polaroid__photo { left: 9px; top: 9px; width: 98px; height: 92px; }
  .polaroid--small .polaroid__name { top: 99px; font-size: 17px; font-weight: 500; }
  .polaroid--small .polaroid__place { top: 119px; font-size: 8px; font-weight: 500; }

  .greeting {
    position: absolute; left: 0; top: 318px; width: 100%;
    text-align: center; color: var(--berry); font-weight: 600;
  }
  .greeting__line { display: block; font-size: 25px; line-height: 34px; }
  .greeting__signature { display: block; font-size: 29px; line-height: 38px; }

  /* Back card */
  .polaroid--large { left: 164px; top: 74px; width: 262px; height: 306px; transform: rotate(-3deg); }
  .polaroid--large .polaroid__photo { left: 14px; top: 17px; width: 234px; height: 218px; }
  .polaroid--large .polaroid__name { top: 236px; font-size: 34px; font-weight: 600; }
  .polaroid--large .polaroid__place { top: 275px; font-size: 22px; font-weight: 600; }
</style>
</head>
<body>
<main class="stage">
  <svg width="0" height="0" style="position:absolute">
    <defs>
      <path id="heart-shape" d="M16 29 C6 21 0 15 0 8.5 C0 3.5 3.8 0 8.3 0 C11.6 0 14.5 2 16 5 C17.5 2 20.4 0 23.7 0 C28.2 0 32 3.5 32 8.5 C32 15 26 21 16 29Z"/>
    </defs>
  </svg>

  <!-- Back side -->
  <section class="card card--back" aria-label="Card back">
    <svg class="heart heart--soft" style="left:-10px;top:-30px;width:70px;height:66px" viewBox="0 0 32 30"><use href="#heart-shape"/></svg>
    <svg class="heart heart--soft" style="left:10px;top:300px;width:150px;height:140px;transform:rotate(-15deg)" viewBox="0 0 32 30"><use href="#heart-shape"/></svg>
    <svg class="heart heart--soft" style="left:525px;top:365px;width:75px;height:70px" viewBox="0 0 32 30"><use href="#heart-shape"/></svg>
    <svg class="line" style="top:30px" viewBox="0 0 585 30" preserveAspectRatio="none"><path d="M0 8 Q290 20 585 22" stroke="var(--string)" stroke-width="3" fill="none"/></svg>

    <figure class="polaroid polaroid--large">
      <span class="polaroid__clip"></span>
      <div class="polaroid__photo" role="img" aria-label="Photo of Phil and Greta"></div>
      <figcaption>
        <span class="polaroid__name">Phil and Greta</span>
        <span class="polaroid__place">Wilmette, IL 2017</span>
      </figcaption>
    </figure>
    <svg class="heart" style="left:132px;top:58px;width:44px;height:42px;transform:rotate(-20deg)" viewBox="0 0 32 30"><use href="#heart-shape"/></svg>
    <svg class="heart" style="left:390px;top:258px;width:56px;height:52px;transform:rotate(12deg)" viewBox="0 0 32 30"><use href="#heart-shape"/></svg>
  </section>

  <!-- Front side -->
  <section class="card card--front" aria-label="Card front">
    <svg class="heart heart--soft" style="left:-5px;top:-25px;width:60px;height:56px" viewBox="0 0 32 30"><use href="#heart-shape"/></svg>
    <svg class="heart heart--soft" style="left:455px;top:-30px;width:150px;height:140px;transform:rotate(10deg)" viewBox="0 0 32 30"><use href="#heart-shape"/></svg>
    <svg class="heart heart--soft" style="left:-10px;top:330px;width:130px;height:120px;transform:rotate(-10deg)" viewBox="0 0 32 30"><use href="#heart-shape"/></svg>
    <svg class="heart heart--soft" style="left:525px;top:365px;width:75px;height:70px" viewBox="0 0 32 30"><use href="#heart-shape"/></svg>

    <h1 class="headline">
      <span class="headline__row">Home <span class="headline__soft">is</span> where</span>
      <span class="headline__row headline__row--second">our hearts <span class="headline__soft">are</span>!</span>
    </h1>

    <svg class="line" style="top:125px" viewBox="0 0 587 30" preserveAspectRatio="none"><path d="M0 12 Q290 22 587 12" stroke="var(--string)" stroke-width="2.5" fill="none"/></svg>

    <figure class="polaroid polaroid--small" style="left:31px;top:152px;transform:rotate(-2deg)">
      <span class="polaroid__clip"></span>
      <div class="polaroid__photo" role="img" aria-label="Photo of Gwen"></div>
      <figcaption><span class="polaroid__name">Gwen,</span><span class="polaroid__place">Washington, DC 2017</span></figcaption>
    </figure>
    <figure class="polaroid polaroid--small" style="left:170px;top:158px;transform:rotate(2deg)">
      <span class="polaroid__clip"></span>
      <div class="polaroid__photo" role="img" aria-label="Photo of Artie"></div>
      <figcaption><span class="polaroid__name">Artie,</span><span class="polaroid__place">New York City 2017</span></figcaption>
    </figure>
    <figure class="polaroid polaroid--small" style="left:311px;top:160px;transform:rotate(-1deg)">
      <span class="polaroid__clip"></span>
      <div class="polaroid__photo" role="img" aria-label="Photo of Marisa"></div>
      <figcaption><span class="polaroid__name">Marisa,</span><span class="polaroid__place">Chicago 2017</span></figcaption>
    </figure>
    <figure class="polaroid polaroid--small" style="left:453px;top:156px;transform:rotate(1deg)">
      <span class="polaroid__clip"></span>
      <div class="polaroid__photo" role="img" aria-label="Photo of Kurt"></div>
      <figcaption><span class="polaroid__name">Kurt,</span><span class="polaroid__place">Worcester, MA 2017</span></figcaption>
    </figure>

    <svg class="heart" style="left:26px;top:140px;width:30px;height:28px;transform:rotate(-15deg)" viewBox="0 0 32 30"><use href="#heart-shape"/></svg>
    <svg class="heart" style="left:257px;top:144px;width:34px;height:32px;transform:rotate(12deg)" viewBox="0 0 32 30"><use href="#heart-shape"/></svg>
    <svg class="heart" style="left:310px;top:236px;width:32px;height:30px;transform:rotate(-8deg)" viewBox="0 0 32 30"><use href="#heart-shape"/></svg>
    <svg class="heart" style="left:443px;top:144px;width:32px;height:30px;transform:rotate(-14deg)" viewBox="0 0 32 30"><use href="#heart-shape"/></svg>

    <p class="greeting">
      <span class="greeting__line">Holiday love and magic from our home to yours,</span>
      <span class="greeting__signature">The Fairbrooks</span>
    </p>
  </section>
</main>
</body>
</html>
```